washable paper bags and accessories

We are three sisters who have discovered a mutual love of bags made from washable paper. It is a brand new business venture for bags, handbags, cosmetic bags, and home storage solutions and décor all made with washable paper.
We would like to have white crumpled paper as a background for both sides. Front of card with the words "plume douce cloth" only in "bohemian typewriter regular" font. Back of card with appointment style format for our next pop up stall
Target Market(s)
mums, females
Industry/Entity Type
Business
Contact Information for Business Card
ph: 0487215364
email:plumedoucecloth@mailbarrow.com

```html
<!DOCTYPE html>
<html lang="en">
<head>
<meta charset="utf-8">
<title>Plume Douce Cloth – Business Card</title>
<link rel="stylesheet" href="https://fonts.googleapis.com/css2?family=Special+Elite&family=Courier+Prime&display=swap">
<style>
  :root {
    --paper-light: #f1efe3;
    --paper-mid: #e2dfcd;
    --paper-shade: #cfcab4;
    --ink: #141311;
    --divider: #1a1917;
  }
  html, body {
    margin: 0;
    padding: 0;
    width: 1200px;
    height: 683px;
    overflow: hidden;
    background: var(--paper-light);
  }
  .business-card {
    position: relative;
    width: 1200px;
    height: 683px;
    overflow: hidden;
    color: var(--ink);
  }
  .paper-texture {
    position: absolute;
    inset: 0;
    width: 100%;
    height: 100%;
  }
  .brand-side {
    position: absolute;
    left: 0;
    top: 0;
    width: 558px;
    height: 683px;
    display: flex;
    align-items: center;
    justify-content: center;
  }
  .brand-name {
    margin: 0;
    margin-top: -30px;
    font-family: "Special Elite", "Courier New", monospace;
    font-weight: 400;
    font-size: 68px;
    line-height: 1.12;
    text-align: center;
    letter-spacing: 1px;
  }
  .divider {
    position: absolute;
    left: 556px;
    top: 42px;
    width: 4px;
    height: 582px;
    background: var(--divider);
  }
  .contact-side {
    position: absolute;
    left: 560px;
    top: 0;
    width: 640px;
    height: 683px;
    text-align: center;
  }
  .contact-heading {
    position: absolute;
    left: 0;
    right: 0;
    top: 76px;
    margin: 0;
    font-family: "Special Elite", "Courier New", monospace;
    font-weight: 400;
    font-size: 45px;
    letter-spacing: 1px;
  }
  .contact-line {
    position: absolute;
    left: 0;
    right: 0;
    margin: 0;
    font-family: "Courier Prime", "Courier New", monospace;
    font-size: 24px;
  }
  .contact-phone { top: 278px; }
  .contact-email { top: 356px; }
</style>
</head>
<body>
  <div class="business-card">
    <svg class="paper-texture" viewBox="0 0 1200 683" preserveAspectRatio="none" role="img" aria-label="White crumpled paper background texture">
      <defs>
        <linearGradient id="paperBase" x1="0" y1="0" x2="1" y2="1">
          <stop offset="0" stop-color="var(--paper-mid)"/>
          <stop offset="0.45" stop-color="var(--paper-light)"/>
          <stop offset="1" stop-color="var(--paper-mid)"/>
        </linearGradient>
        <radialGradient id="paperShade" cx="0.5" cy="0.5" r="0.7">
          <stop offset="0.55" stop-color="var(--paper-shade)" stop-opacity="0"/>
          <stop offset="1" stop-color="var(--paper-shade)" stop-opacity="0.6"/>
        </radialGradient>
      </defs>
      <rect width="1200" height="683" fill="url(#paperBase)"/>
      <rect width="1200" height="683" fill="url(#paperShade)"/>
    </svg>

    <section class="brand-side">
      <h1 class="brand-name">Plume Douce<br>Cloth</h1>
    </section>

    <div class="divider"></div>

    <section class="contact-side">
      <h2 class="contact-heading">Contact information</h2>
      <p class="contact-line contact-phone">Phone: 0487215364</p>
      <p class="contact-line contact-email">Email: plumedoucecloth@mailbarrow.com</p>
    </section>
  </div>
</body>
</html>
```